Brindle Supports

We need an updated website that captures the comprehensive services and supports we provide to persons with developmental disabilities. We need a website design that educates families about the services we provide. We would also need a website that is user-friendly so that we could periodically update training schedules and ongoing programming.

• Thank you for submitting designs.  A few things I am hoping to see offered in the website:
• Front page highlights the services we offer (host homes, family caregiver, day program, employment program, SLS program, supported apartment program, behavior/clinical program)
• Front page also highlights any new programs we want to make prominent:  family caregiver, future restaurant employment openings, etc...
• Interactive Training Calendar
• Employee Resources page (link to carvix, email login, etc.)
• Uniform provider application for host home providers
• Information on agency - history, goals, etc.
• Contact Information/Location

 

Fun things to include:

• Client Highlights (featuring a client story each month, etc...)
• Employee highlights (featuring a staff member...)
• link to other Brindle business pages (Brindle Therapy and Brindle Restaurant)

```html
<!DOCTYPE html>
<html lang="en">
<head>
<meta charset="utf-8">
<title>Brindle Supports</title>
<link href="https://fonts.googleapis.com/css2?family=Roboto:wght@400;500;700&family=Roboto+Slab:wght@400;700&display=swap" rel="stylesheet">
<style>
:root{
  --brand:#8b2c22;
  --brand-dark:#6e2119;
  --nav-top:#a3443a;
  --nav-bottom:#7c2a21;
  --ink:#222;
  --muted:#666;
  --grey-band:#e3e3e3;
  --light-band:#f4f4f4;
  --footer:#1d1d1d;
  --accent-blue:#3f78d0;
  --hero-deep:#0b3a5c;
  --hero-light:#1d7fb2;
}
*{box-sizing:border-box;margin:0;padding:0}
html,body{width:900px;height:1200px;overflow:hidden}
body{position:relative;font-family:"Roboto",Arial,sans-serif;background:#fff;color:var(--ink)}
.abs{position:absolute}
.top-strip{left:0;top:0;width:900px;height:5px;background:#4a1f1a}
.brand{left:150px;top:26px;display:flex;align-items:center;gap:8px;font:700 22px "Roboto",sans-serif;color:var(--brand)}
.brand-dot{width:22px;height:22px;border-radius:50%;background:var(--brand)}
.search{left:530px;top:30px;width:115px;height:16px;border:1px solid #ddd;font-size:6.5px;color:#aaa;padding:4px 5px}
.search-btn{left:645px;top:30px;width:17px;height:16px;background:#444}
.social-top{left:663px;top:30px;display:flex;gap:1px}
.social-top span{width:16px;height:16px;background:var(--brand)}
.contact-line{left:592px;top:53px;font-size:7px;color:#888;display:flex;gap:16px}
.contact-line svg{vertical-align:-1px;margin-right:3px}
.nav{left:0;top:76px;width:900px;height:34px;background:linear-gradient(var(--nav-top),var(--nav-bottom));border-top:2px solid #6a241c}
.nav ul{list-style:none;position:absolute;left:164px;top:0;display:flex;height:32px}
.nav li{color:#fff;font-size:7.5px;font-weight:500;line-height:32px;padding:0 11.5px;border-right:1px solid rgba(0,0,0,.18)}
.nav li.active{background:#2b1512}
.hero{left:0;top:110px;width:900px;height:349px;background:radial-gradient(ellipse at 55% 45%,var(--hero-light),var(--hero-deep) 75%)}
.hero-arrow{top:128px;width:38px;height:41px;background:#111;display:flex;align-items:center;justify-content:center}
.hero-dots{left:416px;top:398px;display:flex;gap:6px}
.hero-dots span{width:9px;height:9px;border-radius:50%;background:#fff}
.hero-dots span.on{background:#c0201a}
.hero-caption{left:0;top:310px;width:900px;height:39px;background:rgba(0,0,0,.45);color:#fff;font-size:18px;text-align:center;line-height:39px}
.welcome h1{left:150px;top:473px;font:400 15px "Roboto",sans-serif;color:var(--brand)}
.welcome p{left:150px;width:380px;font-size:7.2px;line-height:14.4px;color:var(--muted);white-space:nowrap}
.welcome .mission{color:#222}
.more{color:var(--brand);font-size:7.2px}
.welcome-photo{left:537px;top:469px;width:213px;height:118px;background:linear-gradient(100deg,#3a2a20,#8a7260 55%,#d9d2c4 70%,#4a3426);border:2px solid #ddd;box-shadow:0 1px 3px rgba(0,0,0,.3)}
.services{left:0;top:603px;width:900px;height:239px;background:var(--grey-band)}
.section-title{width:900px;left:0;text-align:center;color:var(--brand);font-size:18px;font-weight:400}
.service{width:150px;text-align:center}
.service .icon{width:35px;height:35px;border-radius:50%;background:var(--brand);margin:0 auto;display:flex;align-items:center;justify-content:center}
.service h3{font-size:9px;font-weight:700;margin-top:10px;color:#111}
.service p{font-size:7px;line-height:14.4px;color:var(--muted);margin-top:2px;white-space:nowrap}
.service .more{display:block;margin-top:2px;color:#c0201a}
.view-more{left:394px;top:789px;width:112px;height:31px;background:var(--brand);color:#fff;font-size:8.5px;text-align:center;line-height:31px;box-shadow:0 2px 0 #5a5a5a}
.testimonials{left:0;top:842px;width:900px;height:208px;background:var(--light-band)}
.t-title{letter-spacing:1px;font-size:14px;top:861px}
.t-sub{left:0;width:900px;top:879px;text-align:center;font-size:7px;color:#555}
.t-arrow{top:921px;width:18px;height:18px;border:1px solid var(--accent-blue);background:#fff;display:flex;align-items:center;justify-content:center}
.quote{left:212px;top:915px;width:500px;font:10.8px/18px Arial,sans-serif;letter-spacing:.5px;color:#555;white-space:nowrap}
.author{left:382px;top:988px;width:135px;height:46px;border:1px solid var(--accent-blue);background:#fff}
.author::before{content:"";position:absolute;left:63px;top:-4px;border:4px solid transparent;border-top:0;border-bottom-color:var(--accent-blue)}
.avatar{left:5px;top:4px;width:34px;height:34px;background:linear-gradient(#e9c78a,#c97c4e)}
.author .name{left:53px;top:10px;font:700 9px "Roboto Slab",serif;color:#333}
.author .role{left:53px;top:24px;font-size:6.5px;color:#999}
.footer{left:0;top:1050px;width:900px;height:150px;background:var(--footer)}
.f-item{top:1063px;width:120px;text-align:center;color:#fff;font-size:11.5px}
.f-item svg{display:block;margin:0 auto 6px}
.f-links{left:150px;top:1142px;font-size:7.5px;color:#fff;font-weight:500}
.f-copy{left:150px;top:1161px;font-size:7.5px;color:#fff}
.f-social{left:694px;top:1139px;display:flex;gap:4px}
.f-social span{width:16px;height:16px;border-radius:50%;background:#fff}
</style>
</head>
<body>
<div class="abs top-strip"></div>

<header>
  <div class="abs brand"><span class="brand-dot"></span>Brindle Supports</div>
  <div class="abs search">Search ...</div>
  <div class="abs search-btn"><svg width="17" height="16"><circle cx="8" cy="7.5" r="3" fill="none" stroke="#fff" stroke-width="1.3"/><line x1="10.2" y1="9.7" x2="12" y2="11.5" stroke="#fff" stroke-width="1.4"/></svg></div>
  <div class="abs social-top"><span></span><span></span><span></span><span></span><span></span></div>
  <div class="abs contact-line">
    <span><svg width="7" height="7"><path d="M1 1l2 0 1 2-1 1 2 2 1-1 2 1v2C4 8 1 5 1 1z" fill="#888"/></svg>(555)987-2140</span>
    <span><svg width="8" height="6"><rect width="8" height="6" fill="#888"/><path d="M0 0l4 3 4-3" stroke="#fff" fill="none" stroke-width=".8"/></svg>hello@brindlesupports.org</span>
  </div>
</header>

<nav class="abs nav">
  <ul>
    <li class="active">Home</li><li>Services</li><li>Residental Program</li><li>SLS Program ?</li><li>Become A Provider</li><li>Employee Resources</li><li>Meet ouur Team</li><li>Contact Us</li>
  </ul>
</nav>

<section class="abs hero" role="img" aria-label="Young man in glasses and tweed jacket thinking, in front of a blue digital hexagon background">
  <div class="abs hero-arrow" style="left:0"><svg width="12" height="16"><path d="M9 2L3 8l6 6" stroke="#fff" stroke-width="3" fill="none"/></svg></div>
  <div class="abs hero-arrow" style="right:0"><svg width="12" height="16"><path d="M3 2l6 6-6 6" stroke="#fff" stroke-width="3" fill="none"/></svg></div>
  <div class="abs hero-caption">Building abilities Creating opportunities Developing relationships</div>
</section>
<div class="abs hero-dots"><span class="on"></span><span></span><span></span></div>

<section class="welcome">
  <h1 class="abs">Welcome to Brindle Solutions</h1>
  <p class="abs" style="top:499px">Brindle Supports is an agency designed to creatively serve individuals with developmental disabilities in communi-<br>ty-based settings throughout Alder Valley.&nbsp; Brindle Supports is an approved service agency through the Regional<br>Disability Services Board.</p>
  <p class="abs mission" style="top:548px">Mission Statement: To promote relationships, attachment, positive boundaries, and resource development to<br>create opportunities and improve the lives of people living with disabilities.</p>
  <p class="abs" style="top:579px"><span class="more">Read More +</span></p>
  <div class="abs welcome-photo" role="img" aria-label="Bright living room with sofa, windows and a potted plant"></div>
</section>

<section class="abs services"></section>
<h2 class="abs section-title" style="top:615px">Services</h2>
<div class="abs service" style="left:135px;top:648px">
  <div class="icon"><svg width="22" height="18" fill="#fff"><circle cx="6" cy="4" r="2.5"/><circle cx="11" cy="3" r="2.8"/><circle cx="16" cy="4" r="2.5"/><rect x="3" y="7" width="6" height="9" rx="1.5"/><rect x="8" y="7" width="6" height="10" rx="1.5"/><rect x="13" y="7" width="6" height="9" rx="1.5"/></svg></div>
  <h3>Employment</h3><p>This template was designed specially<br>for you. It's easy to customize<br>anything. Fully responsive layout</p><span class="more">Read More +</span>
</div>
<div class="abs service" style="left:291px;top:648px">
  <div class="icon"><svg width="18" height="18" fill="#fff"><circle cx="9" cy="5" r="4"/><path d="M1 17c0-5 3-7 8-7s8 2 8 7z"/></svg></div>
  <h3>Client Supports</h3><p>This template was designed specially<br>for you. It's easy to customize<br>anything. Fully responsive layout</p><span class="more">Read More +</span>
</div>
<div class="abs service" style="left:448px;top:648px">
  <div class="icon"><svg width="20" height="20"><circle cx="8" cy="12" r="4.5" fill="none" stroke="#fff" stroke-width="3" stroke-dasharray="2.4 1.2"/><circle cx="14.5" cy="5.5" r="3" fill="none" stroke="#fff" stroke-width="2.2" stroke-dasharray="1.8 1"/></svg></div>
  <h3>SLS Services</h3><p>This template was designed specially<br>for you. It's easy to customize<br>anything. Fully responsive layout</p><span class="more">Read More +</span>
</div>
<div class="abs service" style="left:609px;top:648px">
  <div class="icon"><svg width="20" height="16" fill="#fff"><path d="M1 8L10 1l9 7h-2v7H3V8z"/><rect x="6" y="9" width="3" height="3" fill="#8b2c22"/><rect x="11" y="9" width="3" height="3" fill="#8b2c22"/></svg></div>
  <h3>Residential Services</h3><p>This template was designed specially<br>for you. It's easy to customize<br>anything. Fully responsive layout</p><span class="more">Read More +</span>
</div>
<div class="abs view-more">View more</div>

<section class="abs testimonials"></section>
<h2 class="abs section-title t-title">Testmonials</h2>
<div class="abs t-sub">happy Client about us</div>
<div class="abs t-arrow" style="left:159px"><svg width="8" height="10"><path d="M6 1L2 5l4 4" stroke="#3f78d0" stroke-width="1.4" fill="none"/></svg></div>
<div class="abs t-arrow" style="left:722px"><svg width="8" height="10"><path d="M2 1l4 4-4 4" stroke="#3f78d0" stroke-width="1.4" fill="none"/></svg></div>
<p class="abs quote">Lorem ipsum dolor sit amet, consectetur adipiscing elit. Nulla convallis egestas rhoncus.<br>Donec facilisis fermentum sem, ac viverra ante luctus vel. Donec vel mauris quam. Aliquam<br>pellentesque pellentesque turpis, ut bibendum sapien sollicitudin nec.</p>
<div class="abs author">
  <div class="abs avatar" role="img" aria-label="Portrait photo of the client"></div>
  <div class="abs name">Clara Venn</div>
  <div class="abs role">senior designer</div>
</div>

<footer class="abs footer"></footer>
<div class="abs f-item" style="left:114px"><svg width="16" height="16"><path d="M2 2h4l1.5 3.5-2 1.5a9 9 0 004 4l1.5-2L14.5 10.5v3.5C7 14 2 9 2 2z" fill="#fff"/></svg>Talk to u</div>
<div class="abs f-item" style="left:290px"><svg width="18" height="16"><ellipse cx="9" cy="7" rx="8.5" ry="6" fill="#fff"/><path d="M4 11l-2 4 5-3z" fill="#fff"/></svg>Live Chat</div>
<div class="abs f-item" style="left:466px"><svg width="18" height="16"><rect y="2" width="18" height="13" fill="#fff"/><path d="M0 3l9 6 9-6" stroke="#1d1d1d" stroke-width="1.5" fill="none"/></svg>Email Us</div>
<div class="abs f-item" style="left:641px"><svg width="16" height="16" fill="#fff"><rect x="1" y="7" width="3" height="8"/><path d="M5 7l3-6c2 0 2 2 1.5 4H14c1 0 1.5 1 1 2l-2 7c-.3.7-.8 1-1.5 1H5z"/></svg>Good Support</div>
<div class="abs f-links">Home&nbsp; | &nbsp;About Us&nbsp; | &nbsp;Services&nbsp; | &nbsp;<b>News/Blog</b>&nbsp; | &nbsp;<b>Contact Us</b></div>
<div class="abs f-copy">Copyright Brindle Supports.&nbsp; All rights reserved.</div>
<div class="abs f-social"><span></span><span></span><span></span></div>
</body>
</html>
```